Birchwell Pantry Co - labels

I have my logo now so its time to proceed with the labels.
The product is organic juices and smoothies. They will be served in Mason jar's and sold as a premium hand made product into the CBD and outlets around Perth such as yoga studios gyms, cafe's etc. Cleanses to individuals etc.
I have attached the logo and a mock of what I would like to see.
I think the logo and the raw organic, handmade look will work with the Chalkboard design and maybe some bunting to brighten the design.
There is currently approx. 10 Juices and Smoothies to the range so I will need to settle on the design and then have you create a label for each one, once settled on the design.
If you have any questions please let me know.

Text on label:
Raw, Organic, Hand Made, Gluten-Free, Dairy-Free

Juice
Morning Tide Mix
Kale, Apple, Celery, Dandelion, Lemon & Ginger

This product is FRESH. Shake before you enjoy!!!

Label size. highest point for height 70 - 75mm. Length 200mm
I also have more wording and nutritional guide for Australian Standards. I will update soon.
Thank you

    Happy Friday Designers!!!

Well I have just increased the budget to $300. I hope this helps to get some designs coming through. If you need anything else from me please send a message.

I look forward to receiving your designs soon and thank you for working with me on my business. this is such an exciting time for me and you guys are making my dream a reality so thank you for your time.

Regards,

Denise

Reason: I have not received many designs so extending for a few more days.

• Wording - Hand Made
Raw, Organic, Gluten-Free, Dairy-Free
• A chalk board with Juice or Smoothie - Name and ingredients
Bunting I think will work well with the design of logo and chalk board plus bring some colour.

```html
<!DOCTYPE html>
<html lang="en">
<head>
<meta charset="utf-8">
<title>Birchwell Pantry Co – Juice Label</title>
<link rel="stylesheet" href="https://fonts.googleapis.com/css2?family=Archivo+Black&family=Asap:wght@700&family=Magra:wght@700&family=Open+Sans:wght@400;700&display=swap">
<style>
  :root {
    --page: #ffffff;
    --kraft: #c6ad85;
    --olive: #97a03c;
    --olive-deep: #6f7c2e;
    --badge: #e4e63c;
    --ink-green: #1f6a34;
    --title-green: #22a24a;
    --white: #ffffff;
  }
  html, body {
    margin: 0;
    width: 1200px;
    height: 1000px;
    overflow: hidden;
    background: var(--page);
  }
  .canvas { display: block; width: 1200px; height: 1000px; }
  .label-body { fill: var(--kraft); }
  .label-band { fill: var(--olive); }
  .label-tab { fill: var(--olive); }
  .stitch { fill: none; stroke: var(--white); stroke-width: 1.2; stroke-dasharray: 3 3; opacity: .85; }
  .star { fill: var(--white); }
  .badge-disc { fill: var(--badge); }
  .brand-name {
    font-family: "Open Sans", sans-serif;
    font-weight: 700;
    font-size: 12px;
    fill: var(--ink-green);
  }
  .claims {
    font-family: "Open Sans", sans-serif;
    font-weight: 700;
    font-size: 14px;
    fill: var(--ink-green);
    letter-spacing: .4px;
    word-spacing: 5px;
  }
  .product-type {
    font-family: "Archivo Black", sans-serif;
    font-size: 86px;
    fill: var(--olive-deep);
  }
  .product-name {
    font-family: "Magra", sans-serif;
    font-weight: 700;
    font-size: 36px;
    fill: var(--title-green);
  }
  .notice {
    font-family: "Open Sans", sans-serif;
    font-size: 16px;
    fill: var(--ink-green);
  }
  .notice-strong { font-weight: 700; }
  .ingredients {
    font-family: "Asap", sans-serif;
    font-weight: 700;
    font-size: 25px;
    fill: var(--white);
  }
</style>
</head>
<body>
<svg class="canvas" viewBox="0 0 1200 1000" xmlns="http://www.w3.org/2000/svg">
  <defs>
    <filter id="label-shadow" x="-10%" y="-10%" width="120%" height="130%">
      <feDropShadow dx="0" dy="8" stdDeviation="6" flood-color="#000" flood-opacity=".45"/>
    </filter>
  </defs>

  <g class="juice-label" filter="url(#label-shadow)">
    <rect class="label-body" x="100" y="313" width="610" height="442"/>
    <circle class="label-tab" cx="405" cy="318" r="92"/>
    <rect class="label-band" x="100" y="313" width="610" height="26"/>
    <rect class="label-band" x="100" y="710" width="610" height="43"/>
  </g>

  <g class="top-band-details">
    <line class="stitch" x1="100" y1="342" x2="313" y2="342"/>
    <line class="stitch" x1="497" y1="342" x2="710" y2="342"/>
    <circle class="stitch" cx="405" cy="318" r="72"/>
    <g class="stars">
      <polygon class="star" points="120,322 122,327 127,327 123,330 125,335 120,332 115,335 117,330 113,327 118,327"/>
      <polygon class="star" points="165,322 167,327 172,327 168,330 170,335 165,332 160,335 162,330 158,327 163,327"/>
      <polygon class="star" points="210,322 212,327 217,327 213,330 215,335 210,332 205,335 207,330 203,327 208,327"/>
      <polygon class="star" points="255,322 257,327 262,327 258,330 260,335 255,332 250,335 252,330 248,327 253,327"/>
      <polygon class="star" points="298,322 300,327 305,327 301,330 303,335 298,332 293,335 295,330 291,327 296,327"/>
      <polygon class="star" points="512,322 514,327 519,327 515,330 517,335 512,332 507,335 509,330 505,327 510,327"/>
      <polygon class="star" points="556,322 558,327 563,327 559,330 561,335 556,332 551,335 553,330 549,327 554,327"/>
      <polygon class="star" points="601,322 603,327 608,327 604,330 606,335 601,332 596,335 598,330 594,327 599,327"/>
      <polygon class="star" points="646,322 648,327 653,327 649,330 651,335 646,332 641,335 643,330 639,327 644,327"/>
      <polygon class="star" points="690,322 692,327 697,327 693,330 695,335 690,332 685,335 687,330 683,327 688,327"/>
    </g>
  </g>

  <g class="brand-badge">
    <circle class="badge-disc" cx="405" cy="320" r="54"/>
    <text class="brand-name" x="405" y="310" text-anchor="middle">BIRCHWELL</text>
    <text class="brand-name" x="405" y="325" text-anchor="middle">PANTRY</text>
    <text class="brand-name" x="405" y="340" text-anchor="middle">CO</text>
  </g>

  <text class="claims" x="112" y="406">RAW ORGANIC HAND MADE</text>
  <text class="claims" x="698" y="406" text-anchor="end">GLUTEN-FREE DAIRY-FREE</text>

  <text class="product-type" x="260" y="564" textLength="293" lengthAdjust="spacingAndGlyphs">JUICE</text>
  <text class="product-name" x="246" y="616" textLength="318" lengthAdjust="spacing">Morning Tide Mix</text>

  <text class="notice" text-anchor="middle">
    <tspan x="171" y="655">THIS PRODUCT</tspan>
    <tspan x="171" y="673">IS <tspan class="notice-strong">FRESH</tspan></tspan>
  </text>
  <text class="notice" text-anchor="middle">
    <tspan x="642" y="655">SHAKE BEFORE</tspan>
    <tspan x="642" y="673">YOU ENJOY!!!</tspan>
  </text>

  <line class="stitch" x1="100" y1="714" x2="710" y2="714"/>
  <text class="ingredients" x="133" y="741" textLength="553" lengthAdjust="spacingAndGlyphs">Kale, Apple, Celery, Dandelion, Lemon &amp; Ginger</text>
</svg>
</body>
</html>
```